Marketing Flyer for Coaching Company

Need a marketing flyer I can use based off of my website Quintelcoaching.com. Quick Summary of me include "over 40,000 hours of leadership and coaching experience" Talking about the three services offered. Career and life coaching / Open Harbor Hotline / Fractional Sales Leadership. I would love to use the colors from the logo. I do not want pricing included.

Target Market(s)

Therapist Offices and other professional treatment centers

Industry/Entity Type

Coaching

Other font styles liked:
• Hero Light Regular

Colors
0054AA
0677BA
7BADD7
CADEEF
E8F1F8
0094D4
00A9DD
6FCCEA
C7EBF8
E9F6FB
00AB8E
00BBA5
67D7C9
C6EFE9
E9F9F6
59FF00
82FF00
B8FF75
E3FFCB
F4FFEA
FFF300
FFF600
FEFA6F
FFFEC7
FFFEE8
EB3D1F
EC4F4E
F09395
F8D3D4
FCEDEE
E54698
E96AAD
F1A4CE
F9D9EA
FCEFF6
A7469A
B969AE
D3A5CF
EDDBEB
F8F0F9
6B429C
8869AF
B7A5CE
E3DAEB
F3F0F8

Requirements
Must have
• Logo "over 40,000 hours of leadership and coaching experience" Talking about the three services offered. Career and life coaching / Open Harbor Hotline / Fractional Sales Leadership. I would love to use the colors from the logo. Contact info
Nice to have
• Color Pallet based off of logo pallet id's are in the attachments
Should not have
• Pricing

```html
<!DOCTYPE html>
<html lang="en">
<head>
<meta charset="utf-8">
<title>Quintel Coaching Flyer</title>
<link href="https://fonts.googleapis.com/css2?family=Lato:ital,wght@0,400;0,700;0,900;1,400&display=swap" rel="stylesheet">
<style>
  :root {
    --page-bg: #8a8a8a;
    --paper: #ffffff;
    --ink: #111111;
    --brand-navy: #2b2d4f;
    --career: #8d2c8e;
    --hotline: #a6245f;
    --company: #663190;
    --accent-green: #82c341;
    --accent-purple: #a7469a;
    --on-card: #ffffff;
  }
  * { box-sizing: border-box; margin: 0; padding: 0; }
  html, body {
    width: 1200px; height: 1200px; overflow: hidden;
    background: var(--page-bg);
    font-family: "Lato", Arial, sans-serif;
  }
  .flyer {
    position: absolute; left: 220px; top: 62px;
    width: 760px; height: 1075px;
    background: var(--paper);
    overflow: hidden;
  }
  .glow-green {
    position: absolute; left: -120px; top: -120px;
    width: 340px; height: 340px;
    background: radial-gradient(circle at 35% 35%, var(--accent-green) 0%, rgba(130,195,65,0.55) 30%, rgba(255,255,255,0) 68%);
  }
  .glow-purple {
    position: absolute; right: -110px; bottom: -120px;
    width: 380px; height: 340px;
    background: radial-gradient(circle at 62% 62%, var(--accent-purple) 0%, rgba(167,70,154,0.5) 30%, rgba(255,255,255,0) 68%);
  }
  .brand {
    position: absolute; top: 52px; left: 0; width: 100%;
    display: flex; flex-direction: column; align-items: center;
  }
  .brand-dot {
    width: 44px; height: 44px; border-radius: 50%;
    background: var(--brand-navy);
    margin-bottom: 14px;
  }
  .brand-name {
    color: var(--brand-navy);
    font-weight: 400; font-size: 40px; letter-spacing: 1px;
    line-height: 1;
  }
  .tagline {
    position: absolute; top: 204px; width: 100%;
    text-align: center; font-style: italic;
    font-size: 25px; color: var(--ink);
  }
  .service {
    position: absolute; left: 35px; width: 690px; height: 224px;
    border-radius: 26px; color: var(--on-card);
    text-align: center; padding: 38px 40px 0;
  }
  .service--career { top: 252px; background: var(--career); }
  .service--hotline { top: 490px; background: var(--hotline); }
  .service--company { top: 729px; background: var(--company); }
  .service-title {
    font-weight: 900; font-size: 25px; letter-spacing: 0.2px;
    margin-bottom: 18px;
  }
  .service-text { font-size: 12px; line-height: 1.35; }
  .service-text + .service-text { margin-top: 12px; }
  .divider { display: block; }
  .contact {
    position: absolute; top: 976px; left: 0; width: 100%;
    display: flex; justify-content: center; align-items: center; gap: 22px;
  }
  .contact-icon { width: 66px; height: 66px; }
  .contact-phone {
    font-weight: 900; font-size: 46px; color: var(--ink); letter-spacing: 0.5px;
  }
</style>
</head>
<body>
  <main class="flyer">
    <div class="glow-green"></div>
    <div class="glow-purple"></div>

    <header class="brand">
      <span class="brand-dot"></span>
      <span class="brand-name">Quintel Coaching</span>
    </header>

    <p class="tagline">Over 40,000 hours of leadership and coaching experience.</p>

    <section class="service service--career">
      <h2 class="service-title">CAREER COACHING</h2>
      <p class="service-text">Sometimes the work isn't about your job—it's about you. I help leaders at all levels develop the confidence, communication skills, and clarity to show up as their best selves, both professionally and personally.
        <span class="divider">-or-</span>
        Thinking about a major career change? Feeling stuck and ready for something new? I guide professionals through pivotal transitions with the wisdom of someone who's made bold moves himself—and thrived.</p>
    </section>

    <section class="service service--hotline">
      <h2 class="service-title">PROFESSIONAL OPEN HARBOR HOTLINE</h2>
      <p class="service-text">Remember that friend who always seems to know what to say when you're stuck? That's what this is.</p>
      <p class="service-text">Sometimes you don't need a six-month coaching program—you just need someone to talk through one specific challenge.</p>
      <p class="service-text">No long-term commitment. No pressure. Just honest conversation and the kind of guidance you'd get from someone who genuinely cares about seeing you succeed.</p>
    </section>

    <section class="service service--company">
      <h2 class="service-title">COMPANY SUPPORT</h2>
      <p class="service-text">Need senior sales leadership without the full-time commitment? I can step in as your fractional Sales Director, bringing two decades of proven leadership to scale your sales operation, mentor your team, and drive sustainable growth.
        <span class="divider">-or-</span>
        Whether you're building a sales team from scratch or refining your approach, my workshops blend strategic insight with relationship-based selling principles that actually work in today's market.</p>
    </section>

    <footer class="contact">
      <svg class="contact-icon" viewBox="0 0 66 66" aria-hidden="true">
        <circle cx="33" cy="33" r="29" fill="none" stroke="#111" stroke-width="5"/>
        <path d="M22 18 l7 -2 l4 9 l-4 4 c2 5 5 8 10 10 l4 -4 l9 4 l-2 7 c-14 1 -29 -14 -28 -28 z" fill="#111"/>
        <path d="M37 20 a10 10 0 0 1 9 9" fill="none" stroke="#111" stroke-width="3" stroke-linecap="round"/>
        <path d="M37 13 a17 17 0 0 1 16 16" fill="none" stroke="#111" stroke-width="3" stroke-linecap="round"/>
      </svg>
      <span class="contact-phone">314-555-0142</span>
    </footer>
  </main>
</body>
</html>
```